label design needed for beef product

i need a simple nice packaging design like these
https://www.brindlemart-shop.example/Ridge-Larder-Gelatin-Natural-Powder/dp/K7QX4LT915/ref=sr_1_3_a_it?ie=UTF8&qid=1500000001&sr=8-3&keywords=beef+gelatin+powder

My company name is TIRP
See logo
https://www.brindlemart-shop.example/Vitamin-Hyaluronic-Nutrient-Lighten-Circles/dp/K3PZ82HDWQ/ref=sr_1_3_a_it?ie=UTF8&qid=1500000002&sr=8-3&keywords=tirp&th=1

i must have the same logo on the label design ,
see attached for the front wording and the back

the facts or the same as the now

Target Market(s)

Brindlemart,

Industry/Entity Type

Health And Wellness

Font styles to use
Serif
Sans Serif

Colors

Designer to choose colors to be used in the design.

Requirements
Must have
• the logo like it is on the following link
• https://www.brindlemart-shop.example/Vitamin-Hyaluronic-Nutrient-Lighten-Circles/dp/K3PZ82HDWQ/ref=sr_1_3_a_it?ie=UTF8&qid=1500000002&sr=8-3&keywords=tirp&th=1
• I need a professional nice listing
Nice to have
• a nice background the packaging size will be the same as now see below
• https://www.brindlemart-shop.example/Ridge-Larder-Gelatin-Natural-Powder/dp/K7QX4LT915/ref=sr_1_3_a_it?ie=UTF8&qid=1500000003&sr=8-3&keywords=beef+gelatin
• i like that design but i want much more professional to it
Should not have
• will discuss

```html
<!DOCTYPE html>
<html lang="en">
<head>
<meta charset="utf-8">
<title>TIRP Unflavored Beef Gelatin Powder – Pouch Label</title>
<link rel="stylesheet" href="https://fonts.googleapis.com/css2?family=Roboto+Condensed:wght@400;700&family=Pinyon+Script&display=swap">
<style>
  :root {
    --backdrop: #e9e9ea;
    --gold-light: #d9b46a;
    --gold: #c49a48;
    --gold-deep: #a67c30;
    --brown: #4a2b14;
    --brown-deep: #331b0b;
    --orchid: #b36fc0;
    --lilac: #e6c7ea;
    --cream: #fbf6ee;
    --ink-gold: #e8c27a;
  }
  html, body {
    margin: 0;
    padding: 0;
    width: 1200px;
    height: 1200px;
    overflow: hidden;
    background: var(--backdrop);
  }
  .canvas {
    position: relative;
    width: 1200px;
    height: 1200px;
  }
  .pouch-front {
    position: absolute;
    left: 180px;
    top: 80px;
    width: 840px;
    height: 1040px;
    border-radius: 6px;
    overflow: hidden;
    box-shadow: 0 8px 24px rgba(0,0,0,0.12);
  }
  .pouch-art {
    position: absolute;
    inset: 0;
    width: 840px;
    height: 1040px;
  }
  .label-text {
    position: absolute;
    left: 0;
    width: 840px;
    text-align: center;
    font-family: "Roboto Condensed", "Arial Narrow", sans-serif;
    color: var(--cream);
    margin: 0;
  }
  .brand {
    top: 252px;
    display: flex;
    justify-content: center;
    align-items: center;
    gap: 22px;
  }
  .brand-dot {
    width: 58px;
    height: 58px;
    border-radius: 50%;
    border: 5px solid var(--lilac);
    box-sizing: border-box;
  }
  .brand-name {
    font-weight: 400;
    font-size: 66px;
    line-height: 1;
    color: var(--orchid);
    letter-spacing: 1px;
  }
  .product-line {
    font-weight: 700;
    line-height: 1;
  }
  .product-flavor { top: 368px; font-size: 64px; }
  .product-name { top: 440px; font-size: 88px; }
  .product-form { top: 540px; font-size: 64px; }
  .purity {
    top: 628px;
    font-weight: 700;
    font-size: 34px;
    color: var(--ink-gold);
    word-spacing: 8px;
  }
  .purity-note {
    top: 672px;
    font-weight: 700;
    font-size: 24px;
  }
  .tagline {
    top: 892px;
    font-family: "Pinyon Script", cursive;
    font-size: 56px;
    color: var(--lilac);
    font-weight: 400;
  }
  .net-weight {
    top: 980px;
    font-weight: 700;
    font-size: 24px;
  }
</style>
</head>
<body>
<main class="canvas">
  <section class="pouch-front" aria-label="Pouch front label">
    <svg class="pouch-art" viewBox="0 0 840 1040" xmlns="http://www.w3.org/2000/svg" aria-hidden="true">
      <defs>
        <linearGradient id="goldFoil" x1="0" y1="0" x2="1" y2="1">
          <stop offset="0" stop-color="#a67c30"/>
          <stop offset="0.35" stop-color="#d9b46a"/>
          <stop offset="0.7" stop-color="#c49a48"/>
          <stop offset="1" stop-color="#a67c30"/>
        </linearGradient>
        <radialGradient id="brownSeal" cx="0.45" cy="0.4" r="0.7">
          <stop offset="0" stop-color="#5c371a"/>
          <stop offset="1" stop-color="#331b0b"/>
        </radialGradient>
        <linearGradient id="brownBase" x1="0" y1="0" x2="0" y2="1">
          <stop offset="0" stop-color="#4a2b14"/>
          <stop offset="1" stop-color="#331b0b"/>
        </linearGradient>
      </defs>

      <rect class="foil-body" width="840" height="1040" fill="url(#goldFoil)"/>
      <line class="zip-seal" x1="0" y1="110" x2="840" y2="110" stroke="#9a742e" stroke-width="3" opacity="0.6"/>
      <line class="zip-seal" x1="0" y1="118" x2="840" y2="118" stroke="#f0d493" stroke-width="2" opacity="0.5"/>

      <path class="base-band" fill="url(#brownBase)"
            d="M0,600 Q420,1120 840,630 V1040 H0 Z"/>
      <path class="base-swoosh-cream" d="M0,586 Q420,1104 840,616" fill="none" stroke="var(--cream)" stroke-width="7"/>
      <path class="base-swoosh-orchid" d="M0,600 Q420,1120 840,630" fill="none" stroke="var(--orchid)" stroke-width="9"/>

      <circle class="seal-ring-cream" cx="424" cy="496" r="304" fill="none" stroke="var(--cream)" stroke-width="10"/>
      <circle class="seal-ring-orchid" cx="414" cy="504" r="298" fill="none" stroke="var(--orchid)" stroke-width="10"/>
      <circle class="seal" cx="420" cy="500" r="288" fill="url(#brownSeal)"/>
    </svg>

    <div class="label-text brand">
      <span class="brand-dot"></span>
      <span class="brand-name">tirp</span>
    </div>
    <h1 class="label-text product-line product-flavor">UNFLAVORED</h1>
    <h2 class="label-text product-line product-name">BEEF GELATIN</h2>
    <h3 class="label-text product-line product-form">POWDER</h3>
    <p class="label-text purity">100% Pure</p>
    <p class="label-text purity-note">Natural Collagen Protein</p>
    <p class="label-text tagline">Excellent Source of Protein!</p>
    <p class="label-text net-weight">Net Wt. 1 Lb (454 g)</p>
  </section>
</main>
</body>
</html>
```